Transform this table

Please make a 2 page A4 handout from this boring table into an engaging design. The front page can be simple and engaging (a summary of the back where all the detail lives)

Target Market(s)

Business

Requirements
Must have
• Clarity. And impact.
Nice to have
• Icons

```html
<!DOCTYPE html>
<html lang="en">
<head>
<meta charset="utf-8">
<title>Safety Culture Maturity Ladder – Handout</title>
<link href="https://fonts.googleapis.com/css2?family=Lexend:wght@400;600;700&family=Outfit:ital,wght@0,400;0,600;0,700;1,600&family=Oswald:wght@600&display=swap" rel="stylesheet">
<style>
  :root{
    --navy:#154c79;
    --navy-dark:#0f3f68;
    --sky:#4a9bd4;
    --white:#ffffff;
    --stage:#474747;
    --red:#e8202a;
    --orange:#f36b21;
    --amber:#f7941d;
    --gold:#fbb21c;
    --yellow:#ffd400;
    --lemon:#fff200;
    --lime:#d7df23;
    --leaf:#8dc63f;
    --green:#39b54a;
  }
  *{box-sizing:border-box;margin:0;padding:0}
  html,body{width:1162px;height:1200px;overflow:hidden}
  body{background:var(--stage);position:relative;font-family:"Outfit",sans-serif}

  .page{position:absolute;width:1165px;height:823px;transform:scale(.7039);transform-origin:0 0;overflow:hidden}
  .page--front{left:171px;top:13px;background:var(--white)}
  .page--back{left:171px;top:607px;background:var(--white)}
  .page svg.bg{position:absolute;left:0;top:0}

  .title{position:absolute;left:0;right:0;top:10px;text-align:center;font-family:"Lexend",sans-serif;font-weight:600;font-size:35px;color:var(--white);letter-spacing:.3px}

  .slogan{position:absolute;font-family:"Lexend",sans-serif;font-weight:600;white-space:nowrap;transform-origin:center;letter-spacing:.5px}
  .slogan--main{left:474px;top:238px;font-size:31px;color:var(--navy);transform:translate(-50%,-50%) rotate(-15deg)}
  .slogan--sub{left:488px;top:281px;font-size:27px;color:var(--sky);transform:translate(-50%,-50%) rotate(-15deg)}

  .badge{position:absolute;border-radius:50%;border:5px solid var(--white);overflow:hidden;transform:translate(-50%,-50%)}
  .badge span{position:absolute;left:0;right:0;top:50%;transform:translateY(-50%);background:var(--white);text-align:center;font-family:"Oswald",sans-serif;font-weight:600;color:#111;letter-spacing:.2px}
  .badge--lg{width:152px;height:152px}
  .badge--lg span{height:30px;line-height:30px;font-size:22px}
  .badge--sm{width:122px;height:122px}
  .badge--sm span{height:24px;line-height:24px;font-size:17px}
  .badge--vulnerable{background:linear-gradient(20deg,var(--red) 35%,var(--orange))}
  .badge--reactive{background:linear-gradient(20deg,var(--amber) 30%,var(--gold))}
  .badge--compliant{background:linear-gradient(20deg,var(--yellow) 30%,var(--lemon))}
  .badge--proactive{background:linear-gradient(20deg,var(--leaf),var(--lime) 70%)}
  .badge--resilient{background:linear-gradient(20deg,var(--green) 30%,var(--leaf))}

  .caption{position:absolute;transform:translateX(-50%);text-align:center;white-space:nowrap;color:var(--white);font-family:"Lexend",sans-serif;font-weight:600;font-size:14px;line-height:18px}

  .step{position:absolute;background:var(--white);border-radius:18px;color:var(--navy);font-family:"Outfit",sans-serif;font-style:italic;font-weight:600;font-size:13.5px;line-height:16px;text-align:center;display:flex;align-items:center;justify-content:center}

  .credit{position:absolute;left:760px;top:777px;width:400px;text-align:center;color:var(--white);font-family:"Lexend",sans-serif;font-size:15.5px;line-height:20px}

  /* back page */
  .stage-card{position:absolute;top:28px;width:200px;border:1.5px solid var(--white);border-radius:16px;overflow:hidden}
  .stage-card h3{background:var(--white);height:60px;display:flex;align-items:center;justify-content:center;text-align:center;color:var(--navy);font-family:"Lexend",sans-serif;font-weight:600;font-size:12.5px;line-height:15px;padding:0 8px;border-radius:0 0 14px 14px}
  .stage-card ul{list-style:none;padding:8px 10px 0 10px}
  .stage-card li{color:var(--white);font-size:10.5px;line-height:18px}
  .stage-card li::before,.practice li::before{content:"• "}

  .aim{position:absolute;transform:translateX(-50%);text-align:center;white-space:nowrap;color:var(--white);font-family:"Lexend",sans-serif;font-weight:600;font-size:12.5px;line-height:15px}

  .practice{position:absolute;width:200px;bottom:23px;border:1.5px solid var(--sky);border-top-width:1px}
  .practice ul{list-style:none;position:absolute;left:10px;right:8px}
  .practice li{color:var(--navy);font-size:10px;line-height:15.2px}
  .practice li b{font-weight:700}
</style>
</head>
<body>

<!-- FRONT PAGE -->
<section class="page page--front" aria-label="Front page summary">
  <svg class="bg" width="1165" height="823" viewBox="0 0 1165 823">
    <polygon points="0,0 1165,0 1097,67 65,67" fill="var(--sky)"/>
    <polygon points="95,0 1070,0 1015,55 150,55" fill="var(--navy)"/>
    <polygon points="0,577 1165,287 1165,823 0,823" fill="var(--navy)"/>
    <polygon points="0,545 1106,270 1112,234 1165,258 1128,312 1112,302 0,579" fill="var(--sky)"/>
    <line x1="109" y1="359" x2="846" y2="163" stroke="var(--navy)" stroke-width="4"/>
    <polygon points="862,158 832,152 842,178" fill="var(--navy)"/>
    <polygon points="725,765 1165,765 1165,823 700,823" fill="var(--sky)"/>
    <polygon points="745,765 765,765 720,823 700,823" fill="var(--white)"/>
    <g stroke="var(--white)" stroke-width="2.5" stroke-dasharray="7 5" fill="none">
      <path d="M204 684 H391 V641"/>
      <path d="M391 633 H579 V589"/>
      <path d="M579 581 H767 V538"/>
      <path d="M767 530 H954 V487"/>
    </g>
    <g fill="var(--white)">
      <circle cx="204" cy="684" r="6"/><circle cx="391" cy="633" r="6"/>
      <circle cx="579" cy="581" r="6"/><circle cx="767" cy="530" r="6"/>
      <circle cx="954" cy="479" r="6"/>
      <polygon points="391,647 386,657 396,657"/>
      <polygon points="579,595 574,605 584,605"/>
      <polygon points="767,544 762,554 772,554"/>
      <polygon points="954,493 949,503 959,503"/>
    </g>
  </svg>

  <h1 class="title">Safety Culture Maturity Ladder</h1>
  <div class="slogan slogan--main">Improving safety culture</div>
  <div class="slogan slogan--sub">Increasing accountability &amp; reliability</div>

  <div class="badge badge--lg badge--vulnerable" style="left:204px;top:513px"><span>VULNERABLE</span></div>
  <div class="badge badge--lg badge--reactive" style="left:392px;top:461px"><span>REACTIVE</span></div>
  <div class="badge badge--lg badge--compliant" style="left:580px;top:414px"><span>COMPLIANT</span></div>
  <div class="badge badge--lg badge--proactive" style="left:767px;top:367px"><span>PROACTIVE</span></div>
  <div class="badge badge--lg badge--resilient" style="left:954px;top:320px"><span>RESILIENT</span></div>

  <p class="caption" style="left:204px;top:616px">Toxic / No care culture<br>“accidents happen”</p>
  <p class="caption" style="left:392px;top:565px">Blame culture<br>“it was an accident!”</p>
  <p class="caption" style="left:580px;top:513px">Compliance culture<br>“Incidents have causes”</p>
  <p class="caption" style="left:767px;top:462px">Ownership culture<br>“We prevent incidents”</p>
  <p class="caption" style="left:954px;top:415px">Interdependent culture<br>“It’s how we do business.”</p>

  <div class="step" style="left:404px;top:645px;width:176px;height:38px">Wake management &amp;<br>control high risks</div>
  <div class="step" style="left:591px;top:594px;width:176px;height:38px">Standardise processes &amp;<br>gain commitment</div>
  <div class="step" style="left:779px;top:543px;width:176px;height:38px">All team members engaged<br>&amp; all risks controlled</div>
  <div class="step" style="left:967px;top:489px;width:176px;height:38px">Develop consistency &amp;<br>fight complacency</div>

  <p class="credit">Based on the Harrow Institute and Daniel Marsh<br>“hearts and minds” model</p>
</section>

<!-- BACK PAGE -->
<section class="page page--back" aria-label="Back page detail">
  <svg class="bg" width="1165" height="823" viewBox="0 0 1165 823">
    <polygon points="0,0 1165,0 1165,340 0,500" fill="var(--sky)"/>
    <polygon points="0,462 1112,306 1116,299 1164,331 1126,376 1112,358 0,497" fill="var(--navy)"/>
  </svg>

  <article class="stage-card" style="left:58px;height:308px">
    <h3>Toxic / No care culture</h3>
    <ul>
      <li>Apathy / resistance</li><li>Near misses not considered</li><li>Negligence</li><li>Dishonesty</li>
      <li>Hiding of incidents</li><li>Serious injury/health risks are unseen or ignored</li>
      <li>Unfair disciplinary actions</li><li>No or little training</li><li>Poor or no communication</li>
      <li>Production at almost any cost</li><li>“Just get it done” attitude or blatantly unsafe</li>
    </ul>
  </article>
  <article class="stage-card" style="left:267px;height:285px">
    <h3>Blame culture<br>Dependent on natural instincts</h3>
    <ul>
      <li>Accept need to care</li><li>Some near miss reporting</li>
      <li>Some window dressing e.g. pre-inspection cleanups and light duty</li>
      <li>Disciplinary action</li><li>Minimum / inconsistent training</li>
      <li>Some communication on a need to know basis</li>
    </ul>
  </article>
  <article class="stage-card" style="left:475px;height:262px">
    <h3>Compliance culture<br>Supervision dependent</h3>
    <ul>
      <li>Some participation</li><li>Near miss discussions</li><li>Acceptable training / awareness</li>
      <li>Established and good communication channels</li><li>Regular people involvement and focus</li>
    </ul>
  </article>
  <article class="stage-card" style="left:684px;height:238px">
    <h3>Independent &amp; personal ownership culture</h3>
    <ul>
      <li>Involvement at all levels</li><li>Near miss involvement</li><li>High level of training / awareness</li>
      <li>Communication at a high level hiding nothing</li>
    </ul>
  </article>
  <article class="stage-card" style="left:892px;height:217px">
    <h3>Interdependent teams culture</h3>
    <ul>
      <li>Way of life</li><li>Comes natural</li>
      <li>Personal involvement by all to manage risks well and prevent incidents</li>
      <li>Authentic communication throughout culture</li>
    </ul>
  </article>

  <p class="aim" style="left:155px;top:354px">Accept that incidents<br>happen</p>
  <p class="aim" style="left:367px;top:331px">Prevent a similar<br>incident</p>
  <p class="aim" style="left:573px;top:307px">Prevent incidents before<br>they occur</p>
  <p class="aim" style="left:793px;top:282px">Improve the systems</p>
  <p class="aim" style="left:999px;top:256px">Way we do business</p>

  <div class="practice" style="left:58px;top:458px">
    <ul style="top:85px">
      <li>Reactive or unresponsive approach</li><li>No OHS systems</li><li>No risk assessment</li>
      <li>Legal non compliance</li><li>Accept equipment / process decay</li>
      <li>Only fix when broken / unsafe repairs</li><li>Reports are shelved / used irresponsibly</li>
      <li>No or poor investigation</li><li>No monitoring / audits</li><li>Permit non-compliance</li>
      <li>Potential illegal practices</li>
    </ul>
  </div>
  <div class="practice" style="left:267px;top:433px">
    <ul style="top:84px">
      <li>Administrator driven</li><li>Loose systems, elements of an OHS Management System</li>
      <li><b>Reactive risk assessment and control</b></li><li>Minimum legal compliance</li>
      <li>Apply PPE as a way of eliminating exposure</li>
      <li><b>Incident investigation but limited analysis</b></li><li>Focus on what happened</li>
      <li>No systems focus</li><li>Human faults occur</li><li>Ad hoc monitoring / audits</li>
      <li>No occupational hygiene or health initiatives</li><li>Reactive medical monitoring</li>
      <li>Monitoring as per regulations</li>
    </ul>
  </div>
  <div class="practice" style="left:475px;top:408px">
    <ul style="top:86px">
      <li>OHS coordinator driven</li><li>OHS standards system and ISO 9002 or equivalent</li>
      <li><b>Risk assessment through existing systems</b></li><li>Total legal compliance goal</li>
      <li>Strictly enforced the use of PPE</li><li>where required (knowing risk)</li>
      <li><b>Causal incident analysis based on events potential</b></li><li>Info sharing from events</li>
      <li>Planned occupational hygiene / environmental monitoring</li>
      <li>Periodical medical examinations</li><li><b>Planned monitoring / audits</b></li>
      <li>Safety meetings and talks</li><li>Some task observations</li>
    </ul>
  </div>
  <div class="practice" style="left:684px;top:383px">
    <ul style="top:82px">
      <li>Committed leadership at all levels</li><li>Line driven systems improvement</li>
      <li>ISO 14001 and ISO 45001</li><li><b>Pro-active formal risk management</b></li>
      <li>Beyond legal compliance</li>
      <li>Seek to actively engineer out process / equipment inadequacies</li>
      <li><b>Incident learnings shared with all levels</b></li><li>Well designed plans / procedures</li>
      <li><b>Focus on adhering to site plans and procedures</b></li><li>Integrated audits</li>
      <li>Peer evaluations and discussion</li>
    </ul>
  </div>
  <div class="practice" style="left:892px;top:355px">
    <ul style="top:81px">
      <li>Individually internalized</li><li>Inspiring genuine leadership</li>
      <li>No silo thinking or actions</li><li>All staff active, positive, respected, speaking up</li>
      <li>Excellent equipment, ultra-organised</li><li>Integrated management systems</li>
      <li><b>Risk management cycle integrated into all systems</b></li><li>Self regulating style</li>
      <li>Eliminate &amp; prevent problems before they occur</li>
      <li>All threats considered in decision-making</li>
      <li><b>Continually improving through external evaluation / auditing</b></li>
      <li>Multiple positive performance indicators drive PDCA cycle</li>
    </ul>
  </div>

  <div class="badge badge--sm badge--vulnerable" style="left:154px;top:458px"><span>VULNERABLE</span></div>
  <div class="badge badge--sm badge--reactive" style="left:367px;top:433px"><span>REACTIVE</span></div>
  <div class="badge badge--sm badge--compliant" style="left:575px;top:408px"><span>COMPLIANT</span></div>
  <div class="badge badge--sm badge--proactive" style="left:793px;top:383px"><span>PROACTIVE</span></div>
  <div class="badge badge--sm badge--resilient" style="left:999px;top:353px"><span>RESILIENT</span></div>
</section>

</body>
</html>
```